Banksia Hill Medical

Stationary design including letterhead A4, appointment card and with compliments
Updates

Hi Designers, we have some orange boxes in and around our main cross, we would like to see if those boxes could be used s part of the stationary design. Perhaps bouncing along the bottom of the page. Cheers Fay

Target Market(s)

We are a general practice with a wide range of patients.

Industry/Entity Type

Medical

Font styles to use
Serif
Sans Serif

Colors
9ccb3b
f37022
a64599

Requirements
Must have
• Address and contact details
Logo.Address
Shop 4, 28 Banksia Hill, GAWLER SA 5118
Phone 08 85469931
Fax 08 85469978
web site - www.banksiahillmedical.com.au
Nice to have
• We have small boxes in our logo we would like used as a design element of the stationary.
Should not have
• Hard to read, script.

```html
<!DOCTYPE html>
<html lang="en">
<head>
<meta charset="utf-8">
<title>Banksia Hill Medical – Letterhead</title>
<link href="https://fonts.googleapis.com/css2?family=Open+Sans:wght@400;600;700&family=Montserrat:wght@700&family=Great+Vibes&display=swap" rel="stylesheet">
<style>
  :root {
    --green: #9ccb3b;
    --green-deep: #6a9a1a;
    --orange: #f37022;
    --orange-soft: #f9a66f;
    --purple: #a64599;
    --ink: #4a4a4a;
    --ink-dark: #2b2b2b;
    --paper: #ffffff;
    --backdrop: #ececec;
  }
  html, body {
    margin: 0;
    width: 1200px;
    height: 795px;
    overflow: hidden;
    background: var(--backdrop);
  }
  .letterhead {
    position: absolute;
    left: 330px;
    top: 15px;
    width: 540px;
    height: 764px;
    background: var(--paper);
    box-shadow: 0 2px 10px rgba(0,0,0,0.12);
    font-family: "Open Sans", Arial, sans-serif;
    color: var(--ink);
    overflow: hidden;
  }
  .brand {
    position: absolute;
    left: 38px;
    top: 62px;
    display: flex;
    align-items: center;
    gap: 8px;
  }
  .brand-dot {
    width: 26px;
    height: 26px;
    border-radius: 50%;
    background: var(--green);
  }
  .brand-name {
    font-family: "Montserrat", Arial, sans-serif;
    font-weight: 700;
    color: var(--purple);
    line-height: 1;
    font-size: 15px;
    letter-spacing: 0.3px;
  }

  .contact {
    position: absolute;
    left: 318px;
    top: 40px;
    font-size: 6.5px;
    line-height: 1.45;
    color: var(--ink-dark);
  }
  .contact dl { margin: 0 0 5px; display: grid; grid-template-columns: 30px auto; }
  .contact dt { color: var(--purple); font-weight: 600; }
  .contact dd { margin: 0; }
  .contact address { font-style: normal; margin-bottom: 5px; }
  .contact .web { font-weight: 700; }

  .letter {
    position: absolute;
    left: 110px;
    top: 160px;
    width: 370px;
    font-size: 7.6px;
    line-height: 1.7;
  }
  .letter .greeting { font-weight: 700; color: var(--ink-dark); margin: 0 0 12px; font-size: 8.2px; }
  .letter p { margin: 0 0 12px; }

  .sign-off { margin-top: 34px; color: var(--ink-dark); }
  .sign-off .signature { font-family: "Great Vibes", cursive; font-size: 26px; line-height: 1; }
  .sign-off .role { font-weight: 700; font-size: 7.5px; margin-top: 2px; }

  .box-pattern {
    position: absolute;
    right: 14px;
    bottom: 18px;
    width: 130px;
    height: 150px;
    background: linear-gradient(160deg, var(--orange) 0%, var(--orange-soft) 100%);
    opacity: 0.85;
  }
  .bottom-band {
    position: absolute;
    left: 0;
    right: 0;
    bottom: 0;
    height: 7px;
    background: var(--green-deep);
  }
</style>
</head>
<body>
<main class="letterhead">
  <div class="brand">
    <span class="brand-dot"></span>
    <span class="brand-name">Banksia Hill Medical</span>
  </div>

  <section class="contact">
    <dl>
      <dt>PHONE</dt><dd>08 85469931</dd>
      <dt>FAX</dt><dd>08 85469978</dd>
    </dl>
    <address>Shop 4, 28 Banksia Hill,<br>GAWLER SA 5118</address>
    <div class="web">www.banksiahillmedical.com.au</div>
  </section>

  <article class="letter">
    <p class="greeting">Lorem Ipsum,</p>
    <p>Cras mattis consectetur purus sit amet fermentum. Etiam porta sem malesuada magna mollis euismod. Integer posuere erat a ante venenatis dapibus posuere velit aliquet. Cras justo odio, dapibus ac facilisis in, egestas eget quam. Aenean eu leo quam. Pellentesque ornare sem lacinia quam venenatis vestibulum.</p>
    <p>Vivamus sagittis lacus vel augue laoreet rutrum faucibus dolor auctor. Donec sed odio dui. Maecenas faucibus mollis interdum. Morbi leo risus, porta ac consectetur ac, vestibulum at eros. Nullam id dolor id nibh ultricies vehicula ut id elit.</p>
    <p>Donec id elit non mi porta gravida at eget metus. Fusce dapibus, tellus ac cursus commodo, tortor mauris condimentum nibh, ut fermentum massa justo sit amet risus. Cras justo odio, dapibus ac facilisis in, egestas eget quam. Cum sociis natoque penatibus et magnis dis parturient montes, nascetur ridiculus mus.</p>
    <p>Cum sociis natoque penatibus et magnis dis parturient montes, nascetur ridiculus mus. Curabitur blandit tempus porttitor. Aenean lacinia bibendum nulla sed consectetur. Lorem ipsum dolor sit amet, consectetur adipiscing elit.</p>
    <p>Cras justo odio, dapibus ac facilisis in, egestas eget quam. Morbi leo risus, porta ac consectetur ac, vestibulum at eros. Duis mollis, est non commodo luctus, nisi erat porttitor ligula, eget lacinia odio sem nec elit. Integer posuere erat a ante venenatis dapibus posuere velit aliquet. Vivamus sagittis lacus vel augue laoreet rutrum faucibus dolor auctor.</p>

    <div class="sign-off">
      <div class="signature">Your Name</div>
      <div class="role">Company Director</div>
    </div>
  </article>

  <div class="box-pattern" role="img" aria-label="Cluster of small orange outlined squares bouncing up from the bottom edge"></div>

  <div class="bottom-band"></div>
</main>
</body>
</html>
```